Seven Quiet Rooms Poster

Seven Quiet Rooms is reaching out to designers, creatives and fans alike to help create an exciting new poster for the film as part of our Fundvaro campaign.

Seven Quiet Rooms is a multi-protagonist, multicultural, humanist drama inspired by the 2008 Mumbai terrorist attacks. Centering on a group of international tourists trapped in their hotel by Islamic fundamentalists, the film aims to explore the key issues facing our society, concerning atheism, religion, religious extremism and humanism.

The film’s poster will be a critical part of a film’s publicity and marketing portfolio and an important resource for the film to take into our festival campaign and distribution talks. We’re looking for a highly polished design that accurately represents the film and matches the standard of the finished film.

We will be uploading some of the best entries to our Chatterbox page for fans to vote on. If you do not wish for your design to appear on the page, please contact us.

You can find our teaser trailer on the Fundvaro link below. We’ve also provided some reference images (found here: http://lnk.example-short.net/Rk4WpZ) and also stills from the film to provide inspiration (found here: http://lnk.example-short.net/Tm8QvB) - how or if you use them is up to you.

Good luck and get designing!

http://www.fundvaro-example.com/projects/seven-quiet-rooms

Please note: Amber Tide Pictures reserves the right to select all promotional material for theatrical release.

Requirements
Must have
• Size: 27" x 40"
Should not have
• Please do not include the credit block on your designs.

```html
<!DOCTYPE html>
<html lang="en">
<head>
<meta charset="utf-8">
<title>Seven Quiet Rooms — Poster</title>
<link rel="stylesheet" href="https://fonts.googleapis.com/css2?family=Inter:wght@300;400;700&display=swap">
<style>
  :root {
    --ink: #ffffff;
    --haze-teal: #62776f;
    --haze-slate: #6f8290;
    --haze-pale: #e3e9ea;
    --skin-warm: #8a6f5a;
    --skin-deep: #5a4436;
    --hair-dark: #2a2826;
    --shadow-dark: #2f302e;
  }
  html, body {
    margin: 0;
    padding: 0;
    width: 810px;
    height: 1200px;
    overflow: hidden;
    background: var(--shadow-dark);
  }
  .poster {
    position: relative;
    width: 810px;
    height: 1200px;
    overflow: hidden;
    font-family: "Inter", "Helvetica Neue", Arial, sans-serif;
    color: var(--ink);
  }
  .poster__photo {
    position: absolute;
    inset: 0;
    background:
      radial-gradient(ellipse 200px 260px at 60px 1020px, rgba(30,28,26,0.75) 0%, rgba(30,28,26,0) 100%),
      radial-gradient(ellipse 170px 240px at 600px 990px, rgba(30,28,26,0.6) 0%, rgba(30,28,26,0) 100%),
      radial-gradient(ellipse 260px 180px at 320px 1160px, rgba(40,45,38,0.7) 0%, rgba(40,45,38,0) 100%),
      linear-gradient(90deg,
        rgba(75,92,86,0.5) 0%,
        rgba(120,135,132,0.25) 8%,
        rgba(62,76,78,0.5) 16%,
        rgba(95,110,118,0.3) 24%,
        rgba(0,0,0,0) 32%,
        rgba(0,0,0,0) 58%,
        rgba(72,88,104,0.55) 66%,
        rgba(110,125,135,0.3) 74%,
        rgba(190,200,204,0.55) 84%,
        rgba(232,238,240,0.92) 100%),
      radial-gradient(ellipse 200px 560px at 330px 790px,
        var(--skin-warm) 0%,
        rgba(120,98,80,0.8) 40%,
        rgba(90,80,70,0) 100%),
      linear-gradient(180deg,
        var(--haze-teal) 0%,
        var(--haze-slate) 28%,
        #6e6b62 52%,
        #5a5248 78%,
        var(--shadow-dark) 100%);
  }
  .poster__streaks {
    position: absolute;
    inset: 0;
    background:
      repeating-linear-gradient(90deg,
        rgba(255,255,255,0) 0px,
        rgba(255,255,255,0.06) 7px,
        rgba(0,0,0,0.05) 13px,
        rgba(255,255,255,0) 22px,
        rgba(30,40,45,0.08) 31px,
        rgba(255,255,255,0) 41px),
      repeating-linear-gradient(90deg,
        rgba(0,0,0,0) 0px,
        rgba(40,55,65,0.12) 37px,
        rgba(220,230,232,0.07) 61px,
        rgba(0,0,0,0) 97px);
  }
  .poster__grain {
    position: absolute;
    inset: 0;
    width: 810px;
    height: 1200px;
    mix-blend-mode: overlay;
    opacity: 0.55;
  }
  .poster__title-block {
    position: absolute;
    top: 250px;
    left: 0;
    width: 810px;
    text-align: center;
  }
  .poster__title { margin: 0; font-weight: normal; }
  .poster__title-upper {
    display: block;
    font-weight: 300;
    font-size: 38px;
    letter-spacing: 0.2em;
    padding-left: 0.2em;
    line-height: 1;
  }
  .poster__title-main {
    display: block;
    margin-top: 2px;
    font-weight: 700;
    font-size: 112px;
    letter-spacing: 0.01em;
    line-height: 1;
  }
  .poster__credit-lead {
    margin: 20px 0 0;
    font-weight: 400;
    font-size: 9px;
    line-height: 1;
  }
  .poster__director {
    margin: 5px 0 0;
    font-weight: 400;
    font-size: 12px;
    letter-spacing: 0.02em;
    line-height: 1;
  }
</style>
</head>
<body>
  <main class="poster">
    <div class="poster__photo" role="img" aria-label="Full-bleed photograph of a young girl with dark hair, her features smeared by vertical streaks of misty grey-teal light"></div>
    <div class="poster__streaks" aria-hidden="true"></div>
    <svg class="poster__grain" viewBox="0 0 810 1200" aria-hidden="true">
      <filter id="streak-grain">
        <feTurbulence type="fractalNoise" baseFrequency="0.09 0.004" numOctaves="3" seed="7"/>
        <feColorMatrix type="saturate" values="0"/>
      </filter>
      <rect width="810" height="1200" filter="url(#streak-grain)"/>
    </svg>
    <header class="poster__title-block">
      <h1 class="poster__title">
        <span class="poster__title-upper">SEVEN QUIET</span>
        <span class="poster__title-main">ROOMS</span>
      </h1>
      <p class="poster__credit-lead">a film by</p>
      <p class="poster__director">Rowan Ashcombe</p>
    </header>
  </main>
</body>
</html>
```